Web Design for "Global Broadcasting Service Business"

We are a satellite company launching a new exciting brand by the name of "Pelumo". Pelumo is a broadcasting solution provider that gives end-to-end solutions to TV channels and other content providers to deliver and distribute their content globally. Weather it be TV channels that need to be broadcasted in their local regions or internationally, or its collection of news from various locations, or even coverage of special sports or other events, we provide the technology and services to make that happen. This allows the broadcaster to focus on the content rather than worry about the logistics of how it will get to its viewers. We can help place their content to regional cable and satellite operators. Moreover we can provide services for content creation and coverage of major sports, news and special events. Pelumo is one-stop-shop for all broadcast solutions

We want a 20 page static website. I am mentioning certain key competitors of ours so that you can have a look at the comparable look we are anticipating in the design

www.orvenmedia.tv
www.dunharlow.com
www.pembrick.com

Its a global company so the design has to give the same look and feel

Target Market(s)

TV Channel Owners and their Technical Heads

Industry/Entity Type

Business

Requirements
Must have
• We want the designers to submit the home page design first giving us the look and feel of the website design. you can use sample text and any satellite based image to start off. Once we shortlist the best home page designs we will ask you to create the remaining pages.

The most work is on the home page, remaining subsections will only require a change in text and images at most. the overall look and feel of the website including headers and footers will remain the same

```html
<!DOCTYPE html>
<html lang="en">
<head>
<meta charset="utf-8">
<title>Pelumo — Broadcast Solutions</title>
<link href="https://fonts.googleapis.com/css2?family=Open+Sans:wght@400;600&display=swap" rel="stylesheet">
<style>
:root{
  --red:#e8202a;
  --blue:#0b5aa8;
  --green:#8cc63f;
  --ink:#222;
  --text:#555;
  --grey-band:#3b3b3b;
  --side:#e7e7e7;
  --foot:#2f2f2f;
  --foot-bottom:#262626;
  --foot-text:#cfcfcf;
}
*{box-sizing:border-box;margin:0;padding:0}
html,body{width:909px;height:1200px;overflow:hidden;background:#fff}
body{position:relative;font-family:"Open Sans",Arial,sans-serif;color:var(--ink)}
.abs{position:absolute}
/* header */
.brand{left:75px;top:28px;display:flex;align-items:center;gap:8px}
.brand-dot{width:26px;height:26px;border-radius:50%;background:var(--red)}
.brand-name{font-size:26px;font-weight:600;color:#333}
.account{right:78px;top:10px;display:flex;gap:22px;font-size:10.5px;color:#333}
.account span{display:flex;align-items:center;gap:6px}
.account i{display:inline-block;width:9px;height:11px;background:#333;border-radius:2px}
.search{left:656px;top:37px;width:170px;height:22px;border:1px solid #bbb;border-radius:3px;display:flex;overflow:hidden}
.search .field{flex:1;font-size:9px;color:#999;padding:5px 0 0 32px;position:relative}
.search .field svg{position:absolute;left:10px;top:5px}
.search .go{width:31px;background:var(--green);color:#fff;font-size:9px;text-align:center;line-height:21px}
.socials{left:678px;top:77px;display:flex;gap:12px}
.socials b{width:16px;height:16px;background:#8a8a8a;border-radius:3px;display:block}
/* nav */
.nav{left:0;top:108px;width:909px;height:33px;background:var(--red);border-top:1px solid #c4151e}
.nav ul{list-style:none;display:flex;position:absolute;left:71px;top:0;height:32px}
.nav li{color:#fff;font-size:11.5px;line-height:32px;padding:0 17px;border-right:1px solid #b5141b}
.nav li:last-child{border-right:0}
/* hero */
.hero{left:0;top:141px;width:909px;height:302px;background:#060606}
.hero-photo{left:90px;top:0;width:728px;height:280px;background:linear-gradient(180deg,#1c2733 0%,#2f4a5e 35%,#3a3226 70%,#120c08 100%)}
.hero-caption{left:68px;top:270px;color:#fff;font-size:14.5px}
.hero-arrows{left:765px;top:272px;display:flex;gap:14px}
/* feature thumbs */
.features{left:0;top:443px;width:909px;height:114px;background:var(--grey-band)}
.feature{top:14px;width:174px;height:85px;border:2px solid #777;border-radius:6px;overflow:hidden}
.feature .shot{position:absolute;inset:0}
.feature .label{position:absolute;left:0;right:0;bottom:0;height:24px;background:rgba(40,40,40,.75);color:#fff;font-size:12.5px;padding:2px 10px}
/* main */
.section-title{font-size:18.5px;font-weight:400;color:#222}
.section-title em{font-style:normal;color:var(--red)}
.rule{height:0;border-top:1px dotted var(--red)}
.intro{left:76px;top:611px;width:518px;font-size:10.3px;line-height:15.2px;color:var(--text)}
.btn{background:var(--blue);color:#fff;font-size:10px;text-align:center;border-radius:2px}
.event{top:786px;width:160px}
.event .shot{width:158px;height:91px}
.event h3{font-size:12px;font-weight:400;margin-top:8px;color:#222}
.event .date{font-size:8.5px;color:#666;margin-top:2px}
.event p{font-size:8.5px;line-height:13.6px;color:#444;margin-top:7px}
.event .more{font-size:9px;color:var(--red);margin-top:5px;display:flex;align-items:center;gap:8px}
.event .more i{width:9px;height:9px;border-radius:50%;background:var(--blue);display:inline-block}
/* sidebar */
.sidebar{left:622px;top:557px;width:204px;height:456px;background:var(--side)}
.side-head{position:absolute;left:5px;width:193px;height:30px;background:#f6f6f6;color:var(--red);font-size:14px;padding:4px 0 0 26px}
.news-item{position:absolute;left:16px;width:180px;font-size:9.4px;line-height:13.6px;color:#333;padding-left:12px}
.news-item::before,.events li::before{content:"›";position:absolute;left:0;top:-1px;font-size:11px}
.events{position:absolute;left:16px;top:287px;list-style:none;font-size:9.4px;color:#333}
.events li{position:relative;padding-left:12px;height:18px}
/* footer */
.footer{left:0;top:1013px;width:909px;height:140px;background:var(--foot)}
.fcol{top:15px}
.fcol h4{font-size:12px;font-weight:400;color:#e6e6e6;margin-bottom:9px}
.fcol a{display:block;font-size:9.4px;color:var(--foot-text);line-height:16px;text-decoration:none}
.bottom{left:0;top:1153px;width:909px;height:47px;background:var(--foot-bottom);border-top:1px solid #444}
.bottom .circles{position:absolute;left:81px;top:12px;display:flex;gap:2px}
.bottom .circles b{width:24px;height:24px;border-radius:50%;background:#d9d9d9;display:block}
.bottom .circles b:first-child{background:var(--blue)}
.copy{position:absolute;right:73px;top:13px;font-size:9.4px;color:#ddd}
</style>
</head>
<body>

<header>
  <div class="abs brand"><span class="brand-dot"></span><span class="brand-name">Pelumo</span></div>
  <div class="abs account"><span><i></i>Login</span><span><i></i>Register</span></div>
  <div class="abs search">
    <div class="field"><svg width="10" height="10" viewBox="0 0 10 10"><circle cx="4" cy="4" r="3" fill="none" stroke="#888" stroke-width="1.3"/><line x1="6.3" y1="6.3" x2="9.3" y2="9.3" stroke="#888" stroke-width="1.4"/></svg>Search</div>
    <div class="go">GO</div>
  </div>
  <div class="abs socials" aria-label="Social links"><b></b><b></b><b></b><b></b><b></b><b></b></div>
</header>

<nav class="abs nav">
  <ul>
    <li>Home</li><li>Who we are</li><li>Broadcast Solutions</li><li>Regional Distribution</li><li>On-Demand Services</li><li>Global Network</li><li>Beams</li>
  </ul>
</nav>

<section class="abs hero">
  <div class="abs hero-photo" role="img" aria-label="Broadcast control room with a wall of monitors and operators at desks"></div>
  <p class="abs hero-caption">Vivamus at nibh ipsum Curabitur at quam dolor. Integer vestibulum eget diam sed commodo.</p>
  <div class="abs hero-arrows">
    <svg width="16" height="20" viewBox="0 0 16 20"><polyline points="11,2 4,10 11,18" fill="none" stroke="#fff" stroke-width="1.5"/></svg>
    <svg width="16" height="20" viewBox="0 0 16 20"><polyline points="5,2 12,10 5,18" fill="none" stroke="#fff" stroke-width="1.5"/></svg>
  </div>
</section>

<section class="abs features">
  <div class="abs feature" style="left:63px"><div class="shot" role="img" aria-label="Satellite dish antenna under blue sky" style="background:linear-gradient(180deg,#2f6fc4,#8fb6e0 60%,#9a8f80)"></div><div class="label">Teleport Facilities</div></div>
  <div class="abs feature" style="left:259px"><div class="shot" role="img" aria-label="Operators at a broadcast equipment console" style="background:linear-gradient(180deg,#8a8a86,#4d5660 60%,#2a2a2a)"></div><div class="label">Turnaround</div></div>
  <div class="abs feature" style="left:456px"><div class="shot" role="img" aria-label="Communications satellite orbiting in space" style="background:linear-gradient(135deg,#05101f,#1c3a66 55%,#0a1424)"></div><div class="label">MCPC Platforms</div></div>
  <div class="abs feature" style="left:652px"><div class="shot" role="img" aria-label="Playout centre with curved monitor desk" style="background:linear-gradient(180deg,#5a4b48,#9a9a9a 55%,#3a3a3a)"></div><div class="label">HD/3D Playout center</div></div>
</section>

<main>
  <h1 class="abs section-title" style="left:75px;top:576px">Welcome to <em>Pelumo</em></h1>
  <div class="abs rule" style="left:75px;top:601px;width:507px"></div>
  <p class="abs intro">Pelumo is a broadcasting solution provider that gives end-to-end solutions to TV channels and other content providers to deliver and distribute their content globally. Weather it be TV channels that need to be broadcasted in their local regions or internationally, or its collection of news from various locations, or even coverage of special sports or other events, we provide the technology and services to make that happen. Moreover we can provide services for content creation and coverage of major sports, news and special events. Pelumo is one-stop-shop for all broadcast solutions</p>
  <div class="abs btn" style="left:529px;top:699px;width:61px;height:22px;line-height:22px;font-size:11px">More</div>

  <h2 class="abs section-title" style="left:75px;top:741px">Latest <em>Events</em></h2>
  <div class="abs rule" style="left:75px;top:768px;width:507px"></div>

  <article class="abs event" style="left:75px">
    <div class="shot" role="img" aria-label="Editing suite with monitors" style="background:linear-gradient(180deg,#2b3447,#5d6574 50%,#3a1a1a)"></div>
    <h3>Etiam auctor ornare nibh</h3><div class="date">Jan 29, 2014</div>
    <p>Curabitur congue lorem , quis ultrices nibh rhoncus vel. Nunc quis sapien nisl ultrices suscipit sit amet tristique lorem.</p>
    <div class="more">More <i></i></div>
  </article>
  <article class="abs event" style="left:257px">
    <div class="shot" role="img" aria-label="Audience shown on a large display screen" style="background:linear-gradient(135deg,#1e2a44,#4e6a93 50%,#7a5040)"></div>
    <h3>Etiam auctor ornare nibh</h3><div class="date">Jan 29, 2014</div>
    <p>Curabitur congue lorem , quis ultrices nibh rhoncus vel. Nunc quis sapien nisl ultrices suscipit sit amet tristique lorem.</p>
    <div class="more">More <i></i></div>
  </article>
  <article class="abs event" style="left:432px">
    <div class="shot" role="img" aria-label="Staff member in a broadcast operations room" style="background:linear-gradient(180deg,#1f2a3c,#6a6f78 55%,#b9b2a6)"></div>
    <h3>Etiam auctor ornare nibh</h3><div class="date">Jan 29, 2014</div>
    <p>Curabitur congue lorem , quis ultrices nibh rhoncus vel. Nunc quis sapien nisl ultrices suscipit sit amet tristique lorem.</p>
    <div class="more">More <i></i></div>
  </article>
</main>

<aside class="abs sidebar">
  <div class="side-head" style="top:18px">News</div>
  <div class="news-item" style="top:55px">Jan 29, 2014<br>In quis ullamcorper ligula. In augue enim, iaculis eget metus vitae, placerat porttitor quam.</div>
  <div class="abs rule" style="left:12px;top:120px;width:166px;border-color:#888"></div>
  <div class="news-item" style="top:131px">Jan 29, 2014<br>In quis ullamcorper ligula. In augue enim, iaculis eget metus vitae, placerat porttitor quam.</div>
  <div class="abs btn" style="left:102px;top:195px;width:91px;height:21px;line-height:21px">Read More</div>

  <div class="side-head" style="top:242px">Upcoming Events</div>
  <ul class="events">
    <li>Curabitur inec ipsum cursus posuere.</li>
    <li>Aenean tincidunt convallis bibendum.</li>
    <li>Donec dolor magna, placerat velit vitae.</li>
    <li>Pellentesque sodales nec malesuad.</li>
    <li>Aenean tincidunt convallis bibendum.</li>
    <li>Curabitur inec ipsum cursus posuere.</li>
  </ul>
  <div class="abs btn" style="left:102px;top:413px;width:91px;height:21px;line-height:21px">Read More</div>
</aside>

<footer>
  <div class="abs footer">
    <div class="abs fcol" style="left:78px"><h4>Broadcast Solutions</h4><a>Teleport Facilities</a><a>Turnaround</a><a>MCPC Platforms</a><a>HD/3D Playout Center</a></div>
    <div class="abs fcol" style="left:275px"><h4>Regional Distribution</h4><a>Access to Cable &amp; DTH head ends</a><a>Market Analysis Consultancy</a></div>
    <div class="abs fcol" style="left:503px"><h4>On-Demand Services</h4><a>Coverage of News, Sports &amp; Special Events</a><a>HD/3D Transmission Services</a><a>Satellite Usage Capacity</a><a>Master Control Room</a><a>State of the Art Studios</a></div>
    <div class="abs fcol" style="left:769px"><h4>Beams</h4><a>Consumers</a><a>Broadcasters</a></div>
  </div>
  <div class="abs bottom">
    <div class="circles" aria-label="Social links"><b></b><b></b><b></b><b></b><b></b><b></b></div>
    <div class="copy">© 2014 Pelumo, All Rights Reserved</div>
  </div>
</footer>

</body>
</html>
```